Non-Profit Organization Needs WordPress websiteTo Empower Women

Our client is a Non-profit organization that requires a responsively-designed WordPress website to help publish their online magazine. This website will also feature their magazine publication that they publish quarterly. The design will need to be mobile-friendly, so it looks great on all devices.

The main purpose of this site is the following, in order of importance:
1. Educate economically-challenged women to improve their lives with blog content and their online Magazine.
2. Create a Membership community for these women to help one another. THE MAIN CALL-TO-ACTION ON THE SITE IS TO MOTIVATE THE READERS TO JOIN THE FREE MEMBERSHIP COMMUNITY.
3. Recognize and Identify the contributing Organizations, and to motivate the organizations to donate money to the non-profit organization.

Here is information from the client about what they want for their website:
*********************************************************************************************
It needs to have two entrances to content: Organizations & Readers; Don't like cluttered which some magazine formats seem to be. Like edgy, yet feminine. Not sweet. Easy to navigate and find what one comes to find. Colorful.

We need: A Resources area, a Donation button prominently placed on the site, section for archived magazine articles; Place for translated issues. We will want to have a private Membership section on the site. (NOTE: These requests should be used to help create the site's navigation menu.)

Here are example websites the client likes and why. Please use them as inspiration.
http:://www.brindlewave.com color, simple design w cool buttons, uncluttered
http:://www.tolvarick.com emotion with the color, ease of getting around
http:://www.quenderpast7.com the second page has the color sections that take you to next page
http:://www.marrowlightjournal.com not sweetly feminine, perhaps community style
http:://www.pellicrest.net use of clear symbols, newer design/graphics look

Target Market(s)

The website targets 2 different audiences: Organizations that help to provide services and help to the website readers, and the Readers themselves. The Readers are mostly economically-challenged females that need inspiration and help. The Readers should be considered the Primary Target Audience, with the Organizations being secondary.

Industry/Entity Type

Non-Profit

Font styles to use
Sans Serif

Colors
f37022
fece3e

Requirements
Must have
• The final design MUST, MUST, MUST be created using Separate PSD layers for each element and graphic! PLEASE create a professional layer structure within your design, so we can code it properly.

Please do NOT use Graphics/Images where Text should be used. Examples of this are the business address, phone number, etc.

The website home page design should identify its two main audiences, the Organizations and the Readers. The main call to action is to invite the Readers to become free members of their membership community.

There MUST be an area on the home page where their online magazine can be embedded onto their site OR an image button etc that leads to the magazine. They use the http://vondrel.com/ system to create the magazine and then embed the issues on their site. Alternatively, you could create a button, image, area, etc, where the user can click the image and then go to the magazine.

A membership login field OR a button that leads to a Members login area.

A small area on the website that either Adsense or advertising can be used, and this MUST be BELOW the FOLD.

The site must project a sense of hope and/or empowerment for its Readers. The imagery should resonate with females who want to be inspired.
Nice to have
• There should be links or buttons to identify Spanish-speaking Readers and Portuguese-speaking Readers.
Should not have
• NO Gallery Sliders or Photo Sliders

```html
<!DOCTYPE html>
<html lang="en">
<head>
<meta charset="utf-8">
<title>RiseWell Magazine</title>
<link href="https://fonts.googleapis.com/css2?family=Questrial&family=Montserrat:wght@500;700&display=swap" rel="stylesheet">
<style>
:root{
  --orange:#f37022;
  --orange-deep:#e2611a;
  --rust:#c9510f;
  --yellow:#fece3e;
  --yellow-soft:#ffd94f;
  --ink:#1a1a1a;
  --grey-text:#555;
  --panel:#f4f4f4;
  --white:#fff;
}
*{box-sizing:border-box;margin:0;padding:0}
html,body{width:764px;height:1200px;overflow:hidden;background:var(--white)}
body{font-family:"Questrial",sans-serif;color:var(--ink)}
.page{position:relative;width:764px;height:1200px;overflow:hidden}
.abs{position:absolute}

/* hero */
.hero{left:0;top:0;width:764px;height:508px;background:
  radial-gradient(ellipse 260px 300px at 520px 220px,#e9c9a8 0%,#e2c89a 40%,rgba(226,214,120,0) 75%),
  linear-gradient(180deg,#e7ec9a 0%,#dfe67a 45%,#f2d84a 75%,#e9c93a 100%)}
.social-top{left:115px;top:9px;display:flex;gap:8px}
.social-top span{width:19px;height:19px;border-radius:50%;background:#1f5fa8;display:block}
.social-top span:nth-child(2){background:#2aa7df}
.social-top span:nth-child(3){background:#d94a38}
.social-top span:nth-child(4){background:#2c5d8a}
.top-btn{top:8px;height:23px;border-radius:12px;font-size:12px;color:var(--white);display:flex;align-items:center;justify-content:center;border:1px solid rgba(255,255,255,.7)}
.btn-register{left:483px;width:79px;background:var(--orange)}
.btn-login{left:572px;width:80px;background:var(--yellow)}
.logo-box{left:-20px;top:37px;width:436px;height:114px;background:var(--white);border-radius:0 26px 26px 0;display:flex;align-items:center;padding-left:130px;gap:10px}
.logo-box .mark{width:16px;height:16px;border-radius:50%;background:var(--orange)}
.logo-box .brand{font-size:58px;color:var(--orange);letter-spacing:1px}
.headline{left:108px;top:196px;line-height:1}
.headline .l1{font-size:29px}
.headline .l1 b{font-weight:normal;font-size:31px}
.headline .l2{font-size:33px;color:var(--orange);margin-top:8px}
.headline .l2 span{color:var(--ink);font-size:38px}
.headline .l3{font-size:47px;color:var(--orange);margin-top:2px}
.headline .l4{font-size:27px;margin-top:8px;line-height:1.2}
.headline i{font-style:italic}
.hero-btn{top:452px;height:37px;border-radius:19px;font-size:18px;color:var(--white);display:flex;align-items:center;justify-content:center;border:2px solid rgba(255,255,255,.8)}
.hero-donate{left:107px;width:140px;background:var(--yellow)}
.hero-member{left:255px;width:140px;background:var(--orange)}

/* nav */
.nav{left:0;top:508px;width:764px;height:49px;background:var(--orange);display:flex;padding-left:109px;align-items:stretch}
.nav a{color:var(--white);text-decoration:none;font-size:15px;display:flex;align-items:center;padding:0 16px;border-right:1px solid rgba(255,255,255,.15)}
.nav a.active{background:var(--orange-deep)}
.nav .nav-donate{position:absolute;left:554px;top:10px;width:91px;height:29px;border-radius:15px;background:var(--white);color:var(--orange);font-family:"Montserrat",sans-serif;font-weight:700;font-size:13px;display:flex;align-items:center;justify-content:center}

/* welcome */
.welcome h1{font-weight:normal;font-size:22px}
.welcome h1 span{color:var(--orange)}
.welcome{left:113px;top:585px;width:270px}
.welcome p{font-size:9.5px;line-height:1.45;margin-top:8px;color:var(--grey-text)}
.welcome p span{color:var(--orange)}
.read-more{left:111px;top:659px;width:100px;height:26px;border-radius:13px;background:var(--orange);color:var(--white);font-size:11px;display:flex;align-items:center;justify-content:center}
.video{left:392px;top:573px;width:260px;height:126px;border:1px solid #ccc;border-radius:6px;background:linear-gradient(90deg,#f1e8e0 0%,#e8d5c3 60%,#cdb8a6 100%);overflow:hidden}
.video .cover{position:absolute;left:10px;top:6px;width:88px;height:114px;background:linear-gradient(180deg,#8e5aa8 0%,#c94f3c 45%,#5e9a6a 100%)}
.video .play{position:absolute;left:100px;top:34px}

/* magazines */
.mag-band{left:0;top:760px;width:764px;height:85px;background:var(--yellow)}
.mag-title{left:112px;top:733px;font-size:20px}
.mag-text{left:115px;top:771px;width:240px;font-size:9px;line-height:1.55}
.issue{top:718px;width:83px}
.issue .label{height:34px;background:var(--yellow);font-size:10.5px;line-height:1.3;text-align:center;padding-top:4px}
.issue .cover{height:105px;position:relative}
.issue .plus{position:absolute;left:27px;top:38px}
.issue-1{left:367px}.issue-1 .cover{background:linear-gradient(180deg,#f0a030,#d9541e 55%,#7e2a16)}
.issue-2{left:467px}.issue-2 .cover{background:linear-gradient(180deg,#59c2d8,#3b8b8f 55%,#4b3a2c)}
.issue-3{left:567px}.issue-3 .cover{background:linear-gradient(180deg,#b48ad0,#d4a05c 50%,#6bb48a)}

/* blog */
.blog-title{left:111px;top:851px;font-size:21px}
.post{top:883px;display:flex;gap:12px}
.post .avatar{width:72px;height:72px;border-radius:50%;border:3px solid #ddd;flex:none}
.post-1{left:111px}.post-1 .avatar{background:linear-gradient(160deg,#d7c7b8,#a78c76)}
.post-2{left:396px}.post-2 .avatar{background:linear-gradient(160deg,#e8dcc8,#c4463a)}
.post h3{font-weight:normal;color:var(--orange);font-size:17px;margin-top:14px}
.post p{font-size:9px;line-height:1.45;width:185px;color:var(--grey-text)}

/* join */
.join{left:0;top:958px;width:764px;height:50px;background:var(--panel)}
.join-text{left:113px;top:973px;font-size:18px}
.join-text b{color:var(--orange);font-family:"Montserrat",sans-serif;font-weight:700;font-size:16px}
.subscribe-big{left:508px;top:968px;width:144px;height:30px;border-radius:15px;background:var(--rust);color:var(--white);font-family:"Montserrat",sans-serif;font-weight:700;font-size:15px;display:flex;align-items:center;justify-content:center}

/* footer */
.footer{left:0;top:1008px;width:764px;height:158px;background:var(--orange);color:var(--white)}
.fcol h4{font-weight:normal;font-size:16px;margin-bottom:10px}
.f-news{left:108px;top:1036px}
.f-news p{font-size:10px;margin-bottom:6px}
.f-news .field{width:113px;height:22px;background:var(--white);color:var(--orange);font-size:8px;padding:6px 6px}
.f-news .btn{margin-top:6px;width:113px;height:23px;background:var(--rust);border:1px solid rgba(255,255,255,.6);font-family:"Montserrat",sans-serif;font-weight:700;font-size:8px;display:flex;align-items:center;justify-content:center}
.f-mag{left:275px;top:1036px}
.f-mag .grid{display:grid;grid-template-columns:34px 34px;gap:6px 18px}
.f-mag .grid span{width:34px;height:34px;border-radius:50%;border:2px solid var(--white);display:block}
.f-mag .grid span:nth-child(1){background:#7a8fb8}
.f-mag .grid span:nth-child(2){background:#b4709c}
.f-mag .grid span:nth-child(3){background:#d9541e}
.f-mag .grid span:nth-child(4){background:#e4edf0}
.f-social{left:418px;top:1036px}
.f-social li{list-style:none;display:flex;align-items:center;gap:6px;font-size:8.5px;margin-bottom:8px}
.f-social li i{width:13px;height:13px;border-radius:50%;background:var(--white);display:block}
.f-test{left:541px;top:1036px}
.f-test .bubble{width:111px;border:1px solid var(--white);border-radius:8px;font-size:8.5px;line-height:1.3;padding:4px 6px;background:var(--orange-deep)}
.f-test .who{display:flex;align-items:center;gap:8px;margin-top:6px;font-size:8.5px;line-height:1.3}
.f-test .who span{width:34px;height:34px;border-radius:50%;border:2px solid var(--white);background:linear-gradient(160deg,#f1d9b0,#c49a6b);flex:none}
.copyright{left:0;top:1176px;width:764px;text-align:center;font-size:8.5px;color:#888}
</style>
</head>
<body>
<div class="page">

  <div class="abs hero" role="img" aria-label="Photo of a smiling young woman lying in a sunny meadow of yellow flowers"></div>
  <div class="abs social-top" aria-label="Social links"><span></span><span></span><span></span><span></span></div>
  <div class="abs top-btn btn-register">REGISTER</div>
  <div class="abs top-btn btn-login">LOGIN</div>

  <div class="abs logo-box"><span class="brand">RiseWell</span></div>

  <div class="abs headline">
    <div class="l1">The <b>MAGAZINE</b> For</div>
    <div class="l2">Empowerment<span>&amp;</span></div>
    <div class="l3">Enrichment</div>
    <div class="l4">Of Today’s <i>Inner<br>City Women !</i></div>
  </div>
  <div class="abs hero-btn hero-donate">DONATE</div>
  <div class="abs hero-btn hero-member">MEMBERSHIP</div>

  <nav class="abs nav">
    <a class="active" href="#">Home</a>
    <a href="#">About</a>
    <a href="#">Participate</a>
    <a href="#">Resources</a>
    <a href="#">Contact</a>
    <a class="nav-donate" href="#">DONATE</a>
  </nav>

  <section class="abs welcome">
    <h1>Welcome To The <span>RiseWell</span></h1>
    <p><span>RiseWell</span> MAGAZINE is a quarterly publication that exists to empower and enrich today’s inner-city woman. there are several ways you can participate...</p>
  </section>
  <div class="abs read-more">READ MORE</div>

  <div class="abs video">
    <div class="cover" role="img" aria-label="Magazine cover artwork"></div>
    <div class="abs" style="left:100px;top:0;width:160px;height:126px;background:linear-gradient(90deg,#eadbcd,#d4bba4)" role="img" aria-label="Video still of a smiling woman"></div>
    <svg class="play" width="58" height="58" viewBox="0 0 58 58"><circle cx="29" cy="29" r="26" fill="rgba(255,255,255,.85)" stroke="#111" stroke-width="4"/><path d="M22 16 L42 29 L22 42 Z" fill="#111"/></svg>
  </div>

  <div class="abs mag-band"></div>
  <h2 class="abs mag-title" style="font-weight:normal">LATEST MAGAZINES</h2>
  <p class="abs mag-text">You’re here because you care about people in the inner city. You don’t see them as a problem or individuals to ignore. No, like those of us on the RiseWell team, you see wonderful individuals each with a story to tell.</p>

  <div class="abs issue issue-1"><div class="label">RiseWell Spring<br>2014</div><div class="cover" role="img" aria-label="Spring 2014 issue cover"><svg class="plus" width="28" height="28"><circle cx="14" cy="14" r="14" fill="rgba(40,40,40,.75)"/><path d="M14 7v14M7 14h14" stroke="#fff" stroke-width="2"/></svg></div></div>
  <div class="abs issue issue-2"><div class="label">RiseWell Spring<br>2014 Publishing</div><div class="cover" role="img" aria-label="Spring 2014 publishing issue cover"><svg class="plus" width="28" height="28"><circle cx="14" cy="14" r="14" fill="rgba(40,40,40,.75)"/><path d="M14 7v14M7 14h14" stroke="#fff" stroke-width="2"/></svg></div></div>
  <div class="abs issue issue-3"><div class="label">RiseWell Spring<br>2014 Spanish</div><div class="cover" role="img" aria-label="Spring 2014 Spanish issue cover"><svg class="plus" width="28" height="28"><circle cx="14" cy="14" r="14" fill="rgba(40,40,40,.75)"/><path d="M14 7v14M7 14h14" stroke="#fff" stroke-width="2"/></svg></div></div>

  <h2 class="abs blog-title" style="font-weight:normal">BLOG</h2>
  <article class="abs post post-1"><div class="avatar" role="img" aria-label="Portrait photo of a reader"></div><div><h3>RiseWell</h3><p>“Oh, you have Spanish! That is really going to help in one of our neighborhood areas.”</p></div></article>
  <article class="abs post post-2"><div class="avatar" role="img" aria-label="Portrait photo of a reader"></div><div><h3>RiseWell</h3><p>“When’s the next one?” said one lady who gives out extra issues to her neighbors.</p></div></article>

  <div class="abs join"></div>
  <div class="abs join-text">JOIN THE <b>FREE MEMBERSHIP COMMUNITY</b></div>
  <div class="abs subscribe-big">SUBSCRIBE</div>

  <footer class="abs footer"></footer>
  <div class="abs fcol f-news"><h4>NEWSLETTER</h4><p>subscribe the newsletter</p><div class="field">NEWSLETTER</div><div class="btn">SUBSCRIBE</div></div>
  <div class="abs fcol f-mag"><h4>MAGAZINE</h4><div class="grid" role="img" aria-label="Small magazine cover thumbnails"><span></span><span></span><span></span><span></span></div></div>
  <div class="abs fcol f-social"><h4>SOCIAL</h4><ul><li><i></i>CHATTERLY</li><li><i></i>CHIRPNET</li><li><i></i>ORBITY PLUS</li><li><i></i>SNAPVALE</li></ul></div>
  <div class="abs fcol f-test"><h4>TESTIMONIAL</h4><div class="bubble">“Oh, you have Spanish! That is really going to help in one of</div><div class="who"><span role="img" aria-label="Portrait photo of reviewer"></span><div>Dana Morrow,<br>Lanterns of Hope</div></div></div>

  <div class="abs copyright">Copyrights © 2014, RiseWell. All Right Reserved.</div>
</div>
</body>
</html>
```